HIDE WARDEN

Labels for Men's Skin Care. Organic, target 25-35 The label will be 2x3.5 on a 4oz amber bottle. 3 labels with the information shown on the uploaded sample.
Our product is a e-commerce built to help my 24 year old twin sons have a business of their own. Although it will be sold online they will also do foot work and sell to barbers at barber shops using as a mist on customers after shaving. So we want something that will attract male customers and will look good in a modern Barbershop. This is there shot and packaging is very very important. So if you could help us out with a great label we would be working with you in the future for package design. Our line will have several mens Organic natural skin care cleanser, mask toners and moisturizers..Thank you for your help. We also hope to put our products in beauty supply shops. So it needs to stand out as a mans product but still be traditional male product. Oh be creative mind that you are and remember we are trying to build a brand that attracts 25-35 male. Thank you

Hello, I just wanted to let you know that I am up working very late.

for anyone on the other side of the world up and working. I sleep about
3 hours.. So I'll be up for a few more hours and then up again around 5am my time

Good morning... I just wanted to say I will need three labels.. The words on all three are not that different and will fit pretty much the same on all three. So if you could work with one showing how the colors might be a little different on the other two you can do that with just the one label Just to make it easier on you if you like.. we can fix the other two once I find the right label,  Thank you it is 3am here.. still working.. I love it.

Target Market(s)

MALE 25-35

Industry/Entity Type

E-Commerce

Requirements
Must have
• final design must be fitted to the dieline uploaded.

```html
<!DOCTYPE html>
<html lang="en">
<head>
<meta charset="utf-8">
<title>Hide Warden – Daily Shave Fix Label</title>
<link rel="stylesheet" href="https://fonts.googleapis.com/css2?family=Montserrat:wght@300;400;600;700;800&family=Tinos&display=swap">
<style>
  :root {
    --bg: #1b2807;
    --lime: #a8cc37;
    --peach: #fbcf8a;
    --cream: #fbe49b;
    --sand: #e2cf78;
    --olive-dark: #5f7d18;
    --olive-light: #7f9e2a;
  }
  * { margin: 0; padding: 0; box-sizing: border-box; }
  html, body { width: 686px; height: 1200px; overflow: hidden; background: var(--bg); }
  .label {
    position: relative;
    width: 686px;
    height: 1200px;
    background: var(--bg);
    font-family: "Montserrat", sans-serif;
  }
  .brand-name {
    position: absolute;
    left: 25px;
    top: 110px;
    font-weight: 600;
    font-size: 68px;
    line-height: 1;
    color: var(--peach);
    letter-spacing: 4px;
    white-space: nowrap;
  }
  .tagline {
    position: absolute;
    right: 25px;
    top: 196px;
    font-weight: 300;
    font-size: 31px;
    letter-spacing: 6px;
    color: var(--peach);
    white-space: nowrap;
  }
  .accent-band {
    position: absolute;
    left: 0;
    top: 311px;
    width: 686px;
    height: 38px;
    background: linear-gradient(to bottom, var(--olive-light), var(--olive-dark));
  }
  .product-title {
    position: absolute;
    left: 29px;
    top: 388px;
    line-height: 1;
  }
  .product-title .audience {
    display: block;
    font-weight: 800;
    font-size: 62px;
    color: var(--lime);
    letter-spacing: 1px;
    margin-bottom: 6px;
  }
  .product-title .benefit {
    display: block;
    font-weight: 700;
    font-size: 54px;
    color: var(--peach);
    line-height: 62px;
    white-space: nowrap;
  }
  .product-title .plus { color: var(--lime); }
  .product-title .ingredient {
    display: block;
    font-weight: 400;
    font-size: 32px;
    color: var(--lime);
    margin-top: 4px;
  }
  .blend-panel {
    position: absolute;
    left: 0;
    top: 711px;
    width: 615px;
    height: 352px;
    background: linear-gradient(to bottom, var(--lime), var(--sand) 55%, var(--peach));
  }
  .blend-name {
    position: absolute;
    left: 628px;
    top: 711px;
    height: 352px;
    writing-mode: vertical-rl;
    transform: rotate(180deg);
    font-weight: 400;
    font-size: 33px;
    color: var(--lime);
    white-space: nowrap;
    text-align: center;
  }
  .scent {
    position: absolute;
    left: 0;
    width: 686px;
    top: 1098px;
    text-align: center;
    font-weight: 800;
    font-size: 34px;
    letter-spacing: 1px;
    color: var(--cream);
  }
  .scent .plus { color: var(--lime); }
  .volume {
    position: absolute;
    left: 0;
    width: 686px;
    top: 1148px;
    text-align: center;
    font-family: "Tinos", serif;
    font-size: 27px;
    color: var(--cream);
  }
</style>
</head>
<body>
<div class="label">
  <div class="brand-name">HIDE WARDEN</div>
  <div class="tagline">DAILY SHAVE FIX</div>

  <div class="accent-band"></div>

  <h1 class="product-title">
    <span class="audience">MEN’S</span>
    <span class="benefit">Facial Conditioner<span class="plus">+</span></span>
    <span class="benefit">Calms Razor Burn</span>
    <span class="benefit">After Shaving</span>
    <span class="ingredient">with Botanical Healing Mint</span>
  </h1>

  <div class="blend-panel" role="img" aria-label="Decorative horizontal stripe pattern fading from lime green to sand"></div>
  <div class="blend-name">Smooth Skin Blend</div>

  <div class="scent">CRANBERRY <span class="plus">+</span> POMEGRANATE</div>
  <div class="volume">3.5 fl. oz 103ml</div>
</div>
</body>
</html>
```